Executive to COACH PPT needs Power Point Design

I would like a powerpoint showing the words executive morphing into the word coach. There is an example attached with the word women morphing into the word coach. It can be done the same way. i am not concerned about the color or the font. It should take the same number of slides to create the morph. I would like the word to take up a large part of the powerpoint page.

I think the attachment should help you understand exactly what i am looking for. I would like it with the same number of powerpoint slides.

The purpose of these powerpoints is for an executive to see this and to understand that if they are going to succeed as an executive they need to morph into a coach. we spend three days teaching them how to do that.

Target Market(s)

executives that are participating in a workshop to be held around the world.

Font styles to use
Sans Serif

Requirements
Must have
• clear beginning with the word EXECUTIVE, clear ending with the word COACH. the look has to be modern and worldly. it has to be international in its feel.
Nice to have
• great color, attractive font and a real connectivity with the words. Making sure the reader understands exactly what we are trying to do.
Should not have
• drawings or designs other than the words, no extra fuss anywhere other than the words.

```html
<!DOCTYPE html>
<html lang="en">
<head>
<meta charset="utf-8">
<title>Executive to Coach – Slide Morph Sequence</title>
<link href="https://fonts.googleapis.com/css2?family=Oswald:wght@600&family=Titillium+Web:wght@700&display=swap" rel="stylesheet">
<style>
  :root {
    --canvas-bg: #ffffff;
    --title-pink: #f3c9cb;
    --slide-blue: #4d6d8a;
    --slide-edge: rgba(20, 35, 55, 0.45);
    --letter-light: #c9d1e2;
    --letter-light-hi: #e4e9f3;
    --letter-dark: #141a4b;
    --letter-shadow: rgba(10, 20, 35, 0.55);
  }
  * { margin: 0; padding: 0; box-sizing: border-box; }
  html, body {
    width: 960px;
    height: 1200px;
    overflow: hidden;
    background: var(--canvas-bg);
  }
  .sheet {
    position: relative;
    width: 960px;
    height: 1200px;
  }
  .sheet-title {
    position: absolute;
    top: 40px;
    left: 0;
    width: 922px;
    text-align: center;
    font-family: "Titillium Web", sans-serif;
    font-weight: 700;
    font-size: 36px;
    line-height: 1;
    color: var(--title-pink);
  }
  .slide {
    position: absolute;
    width: 444px;
    height: 333px;
    background: var(--slide-blue);
    box-shadow: inset 0 0 10px var(--slide-edge);
    display: flex;
    align-items: center;
    justify-content: center;
  }
  .slide--left { left: 26px; }
  .slide--right { left: 490px; }
  .slide--row1 { top: 117px; }
  .slide--row2 { top: 467px; }
  .slide--row3 { top: 814px; }

  .word {
    font-family: "Oswald", sans-serif;
    font-weight: 600;
    font-size: 88px;
    line-height: 1;
    letter-spacing: -1px;
    white-space: nowrap;
    display: inline-block;
  }
  .letter {
    display: inline-block;
  }
  .letter--light {
    color: var(--letter-light);
    text-shadow:
      -1px -1px 0 var(--letter-light-hi),
      2px 3px 2px var(--letter-shadow),
      4px 6px 8px var(--letter-shadow);
  }
  .letter--dark {
    color: var(--letter-dark);
    text-shadow: 3px 4px 6px var(--letter-shadow);
  }
  .letter--flipped {
    transform: rotate(180deg);
  }

  .slide--finale { display: block; }
  .finale-word {
    position: absolute;
  }
  .finale-word--top { left: 46px; top: 76px; }
  .finale-word--bottom { left: 186px; top: 154px; }
</style>
</head>
<body>
<main class="sheet">
  <h1 class="sheet-title">PPT Design Idea - 01a</h1>

  <section class="slide slide--left slide--row1" aria-label="Slide 1">
    <span class="word"><span class="letter letter--light">EXECUTIVE</span></span>
  </section>

  <section class="slide slide--right slide--row1" aria-label="Slide 2">
    <span class="word"><span class="letter letter--light">CO</span><span class="letter letter--dark">TIV</span></span>
  </section>

  <section class="slide slide--left slide--row2" aria-label="Slide 3">
    <span class="word"><span class="letter letter--light">COA</span><span class="letter letter--dark">IV</span></span>
  </section>

  <section class="slide slide--right slide--row2" aria-label="Slide 4">
    <span class="word"><span class="letter letter--light">COAC</span><span class="letter letter--dark">V</span></span>
  </section>

  <section class="slide slide--left slide--row3" aria-label="Slide 5">
    <span class="word"><span class="letter letter--light">COACH</span></span>
  </section>

  <section class="slide slide--right slide--row3 slide--finale" aria-label="Slide 6">
    <span class="word finale-word finale-word--top"><span class="letter letter--light">EXECUTIVE</span></span>
    <span class="word finale-word finale-word--bottom"><span class="letter letter--light">CO</span><span class="letter letter--light letter--flipped">A</span><span class="letter letter--light">CH</span></span>
  </section>
</main>
</body>
</html>
```